Harbourline Panels Brochure

Harbourline Panels New Brochure Brief
Harbourline Panels are manufacturers of kitchen and wardrobe doors. We have 2 target markets, one is business to business and the other business to residential customers.
The main message of our business to residential is to inform them that they can give their kitchen or wardrobe a facelift by just replacing doors and save thousands of dollars by doing this partial renovation. However, this is in direct conflict with our business to business customers (kitchen and wardrobe companies) who buy doors from us and sell complete new kitchens and built in wardrobes to the same residential customers.
Please find links to the Harbourline Panels brochure and website below for your reference. The current dimensions of the brochure is approx. 21cmH x 29.7cmW. https://harbourlinepanels.com.au/harbourlinepanelsbrochure-2/ https://harbourlinepanels.com.au/
I would like to keep the layout of the brochure internal pages consistent with the current design, however, I am open to your ideas. The orange colour as seen on the front page should be a dominant theme as it’s based on our logo however not too overpowering, I prefer to cover to be white. I would like a new front page design, changing the door photos (they will be shades of white, not coloured) and also delete the words ‘ultimate door collection’. Heading to be along the lines of “Custom made kitchen and wardrobe doors”.
On the internal pages, some new door designs will be added and some deleted. s. We are thinking of changing all the door colours to shades of white but also stating that Harbourline Panels can colour match to any major Australian paint brand.
I would like to include a page for Wardrobe Doors with some photos, text and layout options (photo attached). Please add in the before and after images. Please create a before and after using Rob's kitchen in same layout as wardrobe before and after. Please ensure oven is cut from after image. Please add in the photos attached in this brief.
We would also like to include a FAQs section. Some more text describing our product, such as raw material, thickness of doors, painted or unpainted finish and delivery information is to be added.
Re: the ‘edges’ top of page 3; some will be deleted and one new type of edge will be added.
From page 4 onwards, there are different shapes at the bottom of each door design. We are looking for a new way to communicate this as at the moment it is taking up too much room and people do not readily understand that these door patterns can be supplied in the shapes shown in the little diagrams below them.
Please keep in mind all this information will be given at the time of design. I would like to possibly keep the brochure at 8 pages (as it is now). There may be some other changes along the way as this is still in the preliminary stage. Please include the image of our showroom in the brochure mock up.
I look forward to your reply.
Kind Regards,
Greta
* Please note, the images attach with the individual doors need to be changed to some neutral shades such as white, off white, grey, cream etc (similar to the website: https://harbourlinepanels.com.au/kitchen-doors/)

```html
<!DOCTYPE html>
<html lang="en">
<head>
<meta charset="utf-8">
<title>Harbourline Panels – Page 3</title>
<link rel="stylesheet" href="https://fonts.googleapis.com/css2?family=Fira+Sans:wght@400;900&family=Fira+Sans+Condensed:wght@300;400&display=swap">
<style>
  :root {
    --orange: #f7983a;
    --ink: #111111;
    --white: #ffffff;
    --kitchen-a: #c9b79e;
    --kitchen-b: #8a6a48;
    --bedroom-a: #e6e2ee;
    --bedroom-b: #7a6aa6;
    --door-light: #cdd6d6;
    --door-grey: #7d8b88;
  }
  * { margin: 0; padding: 0; box-sizing: border-box; }
  html, body { width: 1200px; height: 848px; overflow: hidden; background: var(--white); }
  .page { position: relative; width: 1200px; height: 848px; background: var(--white); font-family: "Fira Sans", sans-serif; color: var(--ink); }

  .photo { position: absolute; top: 0; height: 404px; }
  .photo--kitchen { left: 0; width: 600px; background: linear-gradient(160deg, #eef0ec 0%, var(--kitchen-a) 55%, var(--kitchen-b) 100%); }
  .photo--bedroom { left: 600px; width: 600px; background: linear-gradient(200deg, #f4f2f8 0%, var(--bedroom-a) 55%, var(--bedroom-b) 100%); }
  .door-samples { position: absolute; left: 420px; top: 20px; width: 360px; height: 360px; }

  .rule { position: absolute; background: var(--orange); }
  .rule--top-a { left: 0; top: 404px; width: 528px; height: 9px; }
  .rule--top-b { left: 559px; top: 404px; width: 187px; height: 9px; }
  .rule--foot-a { left: 0; top: 780px; width: 335px; height: 29px; }
  .rule--foot-b { left: 345px; top: 780px; width: 306px; height: 29px; }
  .rule--foot-c { left: 661px; top: 780px; width: 108px; height: 29px; }

  .headline { position: absolute; left: 25px; top: 430px; font-weight: 900; font-size: 40px; line-height: 38px; text-transform: uppercase; letter-spacing: 0.2px; }
  .headline .accent { color: var(--orange); }

  .intro, .custom-copy { position: absolute; left: 25px; width: 560px; font-size: 18.5px; line-height: 25px; }
  .intro { top: 535px; }
  .custom-title { position: absolute; left: 23px; top: 630px; font-family: "Fira Sans Condensed", sans-serif; font-weight: 300; font-size: 58px; line-height: 60px; color: var(--orange); letter-spacing: 0.5px; }
  .custom-copy { top: 694px; }

  .page-number { position: absolute; left: 24px; top: 781px; font-size: 20px; line-height: 28px; }

  .range-box { position: absolute; left: 817px; top: 456px; width: 298px; height: 283px; border: 8px solid var(--orange); }
  .range-list { list-style: none; position: absolute; left: 21px; top: 52px; }
  .range-list li { font-size: 19px; line-height: 20px; letter-spacing: 0.4px; text-transform: uppercase; margin-bottom: 29px; white-space: nowrap; }
</style>
</head>
<body>
<div class="page">
  <div class="photo photo--kitchen" role="img" aria-label="Photo of a bright renovated kitchen with white cabinets, dark benchtop, pendant lights and bar stools"></div>
  <div class="photo photo--bedroom" role="img" aria-label="Photo of a bedroom with white built-in wardrobe doors, a lamp and a made bed"></div>
  <svg class="door-samples" viewBox="0 0 360 360" role="img" aria-label="Two sample cabinet doors: a light raised-panel door and a grey shaker door">
    <polygon points="5,10 170,0 180,310 20,318" fill="var(--door-light)"/>
    <polygon points="170,30 345,35 340,345 165,335" fill="var(--door-grey)"/>
  </svg>

  <div class="rule rule--top-a"></div>
  <div class="rule rule--top-b"></div>

  <h1 class="headline">Just replace the doors<br>and <span class="accent">save thousands!</span></h1>
  <p class="intro">For a kitchen renovation or bedroom makeover that is quick and easy, you can simply replace the doors and panels.</p>

  <h2 class="custom-title">CUSTOMISE YOUR DOORS</h2>
  <p class="custom-copy">Do you want a door that’s not featured in our brochure? We can program and produce doors to your specifications.</p>

  <div class="range-box">
    <ul class="range-list">
      <li>- Kitchen doors</li>
      <li>- Wardrobe doors</li>
      <li>- Kitchen accessories</li>
      <li>- Wardrobe accessories</li>
    </ul>
  </div>

  <div class="rule rule--foot-a"></div>
  <div class="rule rule--foot-b"></div>
  <div class="rule rule--foot-c"></div>
  <span class="page-number">3</span>
</div>
</body>
</html>
```